Creative, fresh business card design for Orrin Linings

We need a fresh, creative business card design for Orrin Linings. We are the manufacturer of Orrin Linings in Australia. Wall panels are 2400 x 1200mm panels made from MDF and feature 3D patterns on the face of the panel. The colours to be used are green, silver/grey and white RGB
Red 187
Green 207
Blue 65.

An idea is to possibly use a watermark of one of our designs as a background (like on the "Ferns" design on the left hand side of page 2 of our brochure).

Target Market(s)

Interior designers, architects, builders and home renovators

Industry/Entity Type

Business

Contact Information for Business Card

Details to go on the card are:
Our logo (attached),
Slogan: "Decorative panels for interiors and exteriors",
Contact name,
Position,
Mobile phone number,
Business address,
Business phone,
Business fax,
Website and
Email address.

I have attached a few images of our panels and our brochure for reference.

The colours of the business card should feature our logo colours which are: RGB
Red 187
Green 207
Blue 65

Requirements
Must have
• Very modern fonts and design. Some of the designs shown especially the "Weave" design which is a popular design.
Nice to have
• Creative but simple design. Very contemporary.
Should not have
• Anything ornate or old fashioned.

```html
<!DOCTYPE html>
<html lang="en">
<head>
<meta charset="utf-8">
<title>Orrin Linings – Business Card</title>
<link href="https://fonts.googleapis.com/css2?family=Open+Sans:wght@400;600&family=Raleway:wght@300;400;600&display=swap" rel="stylesheet">
<style>
  :root {
    --lime: #bbcf41;
    --lime-light: #c9dc55;
    --olive: #7d9a2a;
    --olive-dark: #5f7a1f;
    --grey: #8e8e8e;
    --grey-text: #9a9a9a;
    --ink: #444;
    --white: #ffffff;
    --stage: #e9ebe6;
  }
  * { box-sizing: border-box; margin: 0; padding: 0; }
  html, body { width: 1200px; height: 1000px; overflow: hidden; background: var(--stage); }
  .card {
    position: absolute; left: 350px; top: 70px; width: 500px; height: 860px;
    background: var(--white); overflow: hidden;
    box-shadow: 0 10px 30px rgba(0,0,0,.18);
    font-family: "Open Sans", sans-serif;
  }
  .panel-texture {
    position: absolute; left: 0; top: 0; width: 100%; height: 490px;
    background: linear-gradient(135deg, #ffffff 0%, #eeeeee 35%, #fafafa 60%, #e9e9e9 100%);
  }
  .brand { position: absolute; left: 70px; top: 80px; display: flex; align-items: center; gap: 18px; }
  .brand-square { width: 56px; height: 56px; background: var(--lime); }
  .brand-name {
    font-family: "Raleway", sans-serif; font-weight: 400; font-size: 42px;
    color: var(--lime); letter-spacing: 1px;
  }
  .slogan {
    position: absolute; left: 70px; top: 190px; width: 360px;
    font-family: "Raleway", sans-serif; font-weight: 300; font-size: 22px;
    color: var(--grey-text); letter-spacing: 4px; line-height: 1.25;
  }
  .web-band {
    position: absolute; left: 0; top: 300px; width: 100%; height: 38px;
    background: var(--lime); color: var(--white);
    font-size: 16px; letter-spacing: 5px; line-height: 38px; padding-left: 70px;
  }
  .person { position: absolute; left: 60px; top: 375px; border-left: 7px solid var(--lime); padding-left: 24px; }
  .person-name {
    font-family: "Raleway", sans-serif; font-weight: 600; font-size: 38px;
    color: var(--lime); letter-spacing: 1px; line-height: 1.05;
  }
  .person-role { font-size: 20px; color: var(--ink); font-weight: 600; margin-top: 4px; }
  .contact {
    position: absolute; left: 0; top: 490px; width: 100%; height: 370px;
    background: linear-gradient(180deg, var(--lime-light) 0%, var(--lime) 40%, var(--olive) 100%);
  }
  .contact-row { display: flex; height: 92.5px; border-bottom: 1px solid rgba(255,255,255,.12); }
  .contact-row:last-child { border-bottom: 0; }
  .contact-icon {
    width: 110px; display: flex; align-items: center; justify-content: center;
    background: rgba(70,90,10,.12);
  }
  .contact-icon svg { width: 30px; height: 30px; fill: var(--white); }
  .contact-text {
    flex: 1; display: flex; flex-direction: column; justify-content: center;
    padding-left: 28px; color: var(--white); font-size: 19px; line-height: 1.3;
  }
</style>
</head>
<body>
<main class="card">
  <div class="panel-texture" role="img" aria-label="Faint white 3D wall panel pattern background"></div>

  <div class="brand">
    <span class="brand-square"></span>
    <span class="brand-name">Orrin Linings</span>
  </div>
  <p class="slogan">decorative panels for interiors &amp; landscapes</p>

  <div class="web-band">www.orrinlinings.com.au</div>

  <div class="person">
    <h1 class="person-name">DANA HOLLIS</h1>
    <p class="person-role">Director</p>
  </div>

  <section class="contact">
    <div class="contact-row">
      <div class="contact-icon">
        <svg viewBox="0 0 24 24" aria-hidden="true"><path d="M6.6 10.8a15.2 15.2 0 0 0 6.6 6.6l2.2-2.2c.3-.3.7-.4 1-.2 1.1.4 2.3.6 3.6.6.6 0 1 .4 1 1V20c0 .6-.4 1-1 1A17 17 0 0 1 3 4c0-.6.4-1 1-1h3.5c.6 0 1 .4 1 1 0 1.3.2 2.5.6 3.6.1.3 0 .7-.2 1z"/></svg>
      </div>
      <div class="contact-text"><span>+61 3 5550 1842</span><span>+61 4 5550 7316</span></div>
    </div>
    <div class="contact-row">
      <div class="contact-icon">
        <svg viewBox="0 0 24 24" aria-hidden="true"><path d="M2 5h20v14H2z M3.5 6.5v.4l8.5 6.2 8.5-6.2v-.4z" fill-rule="evenodd"/></svg>
      </div>
      <div class="contact-text"><span>dana@orrinlinings.com.au</span></div>
    </div>
    <div class="contact-row">
      <div class="contact-icon">
        <svg viewBox="0 0 24 24" aria-hidden="true"><path d="M7 2h9l3 3v4H7z M3 10h18v10H3z M6 13h4v2H6z M6 16.5h4v1.5H6z M13 13h5v5h-5z"/></svg>
      </div>
      <div class="contact-text"><span>+61 3 5550 1843</span></div>
    </div>
    <div class="contact-row">
      <div class="contact-icon">
        <svg viewBox="0 0 24 24" aria-hidden="true"><path d="M12 2a7 7 0 0 0-7 7c0 5.2 7 13 7 13s7-7.8 7-13a7 7 0 0 0-7-7zm0 9.5A2.5 2.5 0 1 1 12 6.5a2.5 2.5 0 0 1 0 5z"/></svg>
      </div>
      <div class="contact-text"><span>14 Kiln Street, Geelong 3220,</span></div>
    </div>
  </section>
</main>
</body>
</html>
```